design a web site for Vantrel Cable Works

Require a web site for a new business. We design, implement and manage high level and highly secure IT solutions for high end corporates and large government departments. we specialize in Secure Fibre optic products for highly secure LAN environments and data centre expertise

Target Market(s)

High end corporates and large government departments

Industry/Entity Type

IT

Coding

Coded - Design and coding required

Number of Pages Required

5+ page

Font styles to use
Other font styles liked:
• Calibri

Colors
0054AA
0677BA
7BADD7
CADEEF
E8F1F8
EB3D1F
EC4F4E
F09395
F8D3D4
FCEDEE

Requirements
Must have
• High end tech look and feel needs to incorporate the VCW Company Logo Three major sections. Basic all day Fibre solutions for everyone. High end solutions for blue chip customers. And high secure solutions for sensitive customers
Nice to have
• Online catalogue
Should not have
• Mundane or outdated look and feel

```html
<!DOCTYPE html>
<html lang="en">
<head>
<meta charset="utf-8">
<title>Vantrel Cable Works</title>
<link rel="stylesheet" href="https://fonts.googleapis.com/css2?family=Poppins:wght@400;500;600&family=Lato:wght@400;700&display=swap">
<style>
:root{
  --navy:#0c2460;
  --red:#b5192d;
  --ink:#1d1d1f;
  --body:#3a3a3a;
  --white:#ffffff;
  --rule:#d9d9d9;
  --hero-a:#0d2a44;
  --hero-b:#3f6b86;
}
*{margin:0;padding:0;box-sizing:border-box}
html,body{width:1200px;height:3236px;overflow:hidden;background:var(--white)}
body{font-family:"Lato",sans-serif;color:var(--ink);position:relative}
.abs{position:absolute}
/* header */
.site-header{position:absolute;left:0;top:0;width:1200px;height:99px;background:var(--white)}
.brand{position:absolute;display:flex;align-items:center;gap:12px}
.brand-mark{width:44px;height:44px;background:var(--navy)}
.brand-name{font-family:"Poppins",sans-serif;font-weight:600;color:var(--navy);letter-spacing:1px;text-transform:uppercase}
.site-header .brand{left:116px;top:26px}
.site-header .brand-name{font-size:21px}
.main-nav{position:absolute;top:38px;left:499px;display:flex;gap:37px;font-family:"Poppins",sans-serif;font-size:16px;color:var(--navy)}
.main-nav a{color:inherit;text-decoration:none}
.main-nav .active{font-weight:600;font-size:17px;border-bottom:1.5px solid var(--navy);padding-bottom:3px}
/* hero */
.hero{position:absolute;left:0;top:99px;width:1200px;height:608px;background:linear-gradient(100deg,var(--hero-a) 0%,#1b4564 45%,var(--hero-b) 100%)}
.hero-title{position:absolute;left:111px;top:116px;font-family:"Poppins",sans-serif;font-weight:600;font-size:50px;color:var(--white);letter-spacing:.5px}
.hero-sub{position:absolute;left:113px;top:183px;font-family:"Poppins",sans-serif;font-weight:600;font-size:30px;color:var(--white)}
.hero-text{position:absolute;left:113px;top:234px;width:480px;font-size:16px;line-height:31px;color:var(--white)}
.btn{display:flex;align-items:center;justify-content:center;font-family:"Poppins",sans-serif;font-weight:500;text-decoration:none}
.hero .btn{position:absolute;left:112px;top:321px;width:153px;height:49px;background:var(--white);color:var(--navy);font-size:17px}
/* about */
.about{position:absolute;left:0;top:707px;width:1200px;height:517px;text-align:center}
.about h2{position:absolute;left:0;right:0;top:62px;font-family:"Poppins",sans-serif;font-weight:500;font-size:33px;color:var(--ink)}
.about p{position:absolute;left:150px;right:150px;font-size:17px;line-height:31px;color:var(--body)}
.about .p1{top:120px}
.about .p2{top:243px}
.about .btn{position:absolute;left:516px;top:372px;width:171px;height:58px;background:var(--navy);color:var(--white);font-size:17px}
/* feature bands */
.feature{position:absolute;left:0;width:1200px}
.feature-copy,.feature-media{position:absolute;top:0;width:600px;height:100%}
.feature-copy{color:var(--white);padding:62px 0 0 76px}
.feature-copy h3{font-family:"Poppins",sans-serif;font-weight:500;font-size:32px;line-height:41px;margin-bottom:10px}
.feature-copy p{font-size:16px;line-height:31px;width:470px}
.feature-copy .btn{margin-top:26px;width:155px;height:49px;background:var(--white);font-size:17px}
.is-red{background:var(--red)}
.is-red .btn{color:var(--red)}
.is-navy{background:var(--navy)}
.is-navy .btn{color:var(--navy)}
/* footer */
.site-footer{position:absolute;left:0;top:2713px;width:1200px;height:523px}
.footer-brand{position:absolute;left:110px;top:70px;width:240px}
.footer-brand .brand{position:relative;flex-direction:column;align-items:flex-start;gap:10px}
.footer-brand .brand-mark{width:64px;height:64px}
.footer-brand .brand-name{font-size:21px}
.footer-brand p{margin-top:14px;padding-left:5px;font-size:16px;line-height:30px;color:var(--body)}
.socials{position:absolute;left:114px;top:317px;display:flex;gap:13px}
.socials span{width:24px;height:24px;border-radius:50%;background:var(--ink)}
.footer-col{position:absolute;top:128px;font-family:"Lato",sans-serif}
.footer-col h4{font-family:"Poppins",sans-serif;font-weight:500;font-size:19px;color:var(--ink);margin-bottom:22px}
.links li{list-style:none;font-size:16px;line-height:31px;color:var(--ink)}
.links li::before{content:"<<";font-size:10px;letter-spacing:-1px;margin-right:12px;vertical-align:2px}
.contact li{list-style:none;display:flex;gap:10px;font-size:16px;line-height:31px;margin-bottom:10px;color:var(--ink)}
.contact svg{flex:none;margin-top:8px}
.subscribe p{font-size:16px;line-height:28px;width:250px;color:var(--ink)}
.subscribe .field{margin-top:18px;width:253px;height:49px;border:1px solid #555;padding-left:13px;display:flex;align-items:center;font-size:15px;color:var(--ink)}
.subscribe .btn{margin-top:20px;width:169px;height:48px;background:var(--navy);color:var(--white);font-size:19px}
.footer-rule{position:absolute;left:0;top:447px;width:1200px;height:1px;background:#9a9a9a}
.copyright{position:absolute;left:0;right:0;top:478px;text-align:center;font-size:15px;color:var(--ink)}
</style>
</head>
<body>
<header class="site-header">
  <div class="brand"><span class="brand-mark"></span><span class="brand-name">Vantrel Cable Works</span></div>
  <nav class="main-nav">
    <a class="active" href="#">Home</a>
    <a href="#">Fiber Solutions</a>
    <a href="#">Blue Chip Customers</a>
    <a href="#">Sensitive Customers</a>
  </nav>
</header>

<section class="hero" role="img" aria-label="Photo of two engineers smiling at a laptop in a data centre">
  <h1 class="hero-title">VANTREL CABLE WORKS</h1>
  <p class="hero-sub">HIGH - SIOS IT SOLUTIONS</p>
  <p class="hero-text">Implement and manage high-level and highly secure IT solutions for high-end corporates and large government departments</p>
  <a class="btn" href="#">Get Started</a>
</section>

<section class="about">
  <h2>About Us</h2>
  <p class="p1">Lorem ipsum dolor sit amet, consectetur adipiscing elit, sed do eiusmod tempor incididunt ut labore et dolore magna aliqua. Ut enim ad minim veniam, quis nostrud exercitation ullamco laboris nisi ut aliquip ex ea commodo consequat. Duis aute irure dolor in reprehenderit in voluptate velit esse cillum dolore eu fugiat nulla pariatur.</p>
  <p class="p2">Excepteur sint occaecat cupidatat non proident, sunt in culpa qui officia deserunt mollit anim id est laborum."Sed ut perspiciatis unde omnis iste natus error sit voluptatem accusantium doloremque laudantium, totam rem aperiam, eaque ipsa quae ab illo inventore veritatis et quasi architecto beatae vitae dicta sunt explicabo.</p>
  <a class="btn" href="#">Read More</a>
</section>

<section class="feature" style="top:1224px;height:496px">
  <div class="feature-copy is-red" style="left:0">
    <h3>Basic all-day Fibre<br>solutions for everyone</h3>
    <p>Lorem ipsum dolor sit amet, consectetur adipiscing elit, sed do eiusmod tempor incididunt ut labore et dolore magna aliqua. ad minim veniam, quis nostrud exercitation ullamco laboris nisi ut aliquip ex ea commodo consequat. Duis aute irure dolor in reprehenderit in voluptate velit esse cillum dolore eu fugiat nulla pariatur. Excepteur sint occaecat cupidatat non proident, sunt in culpa qui officia deserunt mollit anim id est laborum.</p>
    <a class="btn" href="#">Read More</a>
  </div>
  <div class="feature-media" style="left:600px;background:linear-gradient(120deg,#2d3fd0 0%,#1b2a7a 45%,#2f8a3a 100%)" role="img" aria-label="Photo of a hand connecting labelled fibre patch cables in a server rack"></div>
</section>

<section class="feature" style="top:1720px;height:499px">
  <div class="feature-media" style="left:0;background:linear-gradient(135deg,#e6e6ea 0%,#9ab4d8 45%,#3a4a66 100%)" role="img" aria-label="Photo of a hand swiping a blue card through a payment terminal"></div>
  <div class="feature-copy is-navy" style="left:600px;padding-left:76px">
    <h3>High-end solutions for<br>&nbsp;blue chip customers</h3>
    <p>Lorem ipsum dolor sit amet, consectetur adipiscing elit, sed do eiusmod tempor incididunt ut labore et dolore magna aliqua. ad minim veniam, quis nostrud exercitation ullamco laboris nisi ut aliquip ex ea commodo consequat. Duis aute irure dolor in reprehenderit in voluptate velit esse cillum dolore eu fugiat nulla pariatur. Excepteur sint occaecat cupidatat non proident, sunt in culpa qui officia deserunt mollit anim id est laborum.</p>
    <a class="btn" href="#">Read More</a>
  </div>
</section>

<section class="feature" style="top:2219px;height:494px">
  <div class="feature-copy is-red" style="left:0">
    <h3>High-secure solutions<br>for sensitive customers</h3>
    <p>Lorem ipsum dolor sit amet, consectetur adipiscing elit, sed do eiusmod tempor incididunt ut labore et dolore magna aliqua. ad minim veniam, quis nostrud exercitation ullamco laboris nisi ut aliquip ex ea commodo consequat. Duis aute irure dolor in reprehenderit in voluptate velit esse cillum dolore eu fugiat nulla pariatur. Excepteur sint occaecat cupidatat non proident, sunt in culpa qui officia deserunt mollit anim id est laborum.</p>
    <a class="btn" href="#">Read More</a>
  </div>
  <div class="feature-media" style="left:600px;background:linear-gradient(110deg,#1f4450 0%,#3b6b78 50%,#2a4a58 100%)" role="img" aria-label="Photo of a person touching a digital file and cloud storage diagram"></div>
</section>

<footer class="site-footer">
  <div class="footer-brand">
    <div class="brand"><span class="brand-mark"></span><span class="brand-name">Vantrel Cable Works</span></div>
    <p>Excepteur sint occaecat cupidatat non proident,</p>
  </div>
  <div class="socials" aria-label="Social links"><span></span><span></span><span></span><span></span></div>

  <div class="footer-col" style="left:391px">
    <h4>Quick Links</h4>
    <ul class="links">
      <li>Home</li><li>About Us</li><li>Fiber solution</li><li>Blue chip</li><li>Sensitive Customer</li>
    </ul>
  </div>

  <div class="footer-col" style="left:592px">
    <h4>Contact Us</h4>
    <ul class="contact">
      <li><svg width="13" height="13" viewBox="0 0 24 24"><path fill="#1d1d1f" d="M6.6 10.8a15.1 15.1 0 0 0 6.6 6.6l2.2-2.2c.3-.3.7-.4 1-.2 1.1.4 2.3.6 3.6.6.6 0 1 .4 1 1V20c0 .6-.4 1-1 1C10.6 21 3 13.4 3 4c0-.6.4-1 1-1h3.5c.6 0 1 .4 1 1 0 1.3.2 2.5.6 3.6.1.3 0 .7-.2 1z"/></svg>+1 5550 142 7788</li>
      <li><svg width="14" height="12" viewBox="0 0 24 20"><path fill="#1d1d1f" d="M2 2h20v16H2z"/><path fill="none" stroke="#fff" stroke-width="2" d="M2 3l10 8 10-8"/></svg>info@vantrelcable.com</li>
      <li><svg width="13" height="17" viewBox="0 0 24 32"><path fill="#1d1d1f" d="M12 0C5.4 0 0 5.4 0 12c0 9 12 20 12 20s12-11 12-20C24 5.4 18.6 0 12 0zm0 17a5 5 0 1 1 0-10 5 5 0 0 1 0 10z"/></svg><span>Vantrel Cable Works,United<br>States.</span></li>
    </ul>
  </div>

  <div class="footer-col subscribe" style="left:834px">
    <h4>Subscribe</h4>
    <p>Sign up to hear about insurance news.</p>
    <div class="field">Email</div>
    <a class="btn" href="#">Sign Up</a>
  </div>

  <div class="footer-rule"></div>
  <p class="copyright">Copyrights@2022.Vantrel Cable Works.Allrightsreserved</p>
</footer>
</body>
</html>
```